New website for Holloway Law Firm at www.keepfirmplan.example

We are a professional law firm located in the Nashville, Tennessee USA area. We focus on personal injury law. We are looking for a slick new website that is user friendly for updating with new blogs, videos, etc. The primary colors should be red, black, and white. It should load extremely fast and have a good mobile component. The pages for the design will include a home page, about us, news, contact us, and practice page. The practice page will be copied for all the practice areas including motor vehicle accidents, slip and fall accidents, dog bites, etc. We have included an image which we would like to include in the new site which shows the color scheme The image is called banner-Car Wreck. The new website should NOT have gavels, court houses, law books, scales or the typical images for a law firm.

Target Market(s)

People in Tennessee involved in accidents

Industry/Entity Type

Legal services, law firm

Number of Pages Required

5+ page

Font styles to use
Serif

Colors
EB3D1F
EC4F4E
F09395
F8D3D4
FCEDEE

Requirements
Should not have
• Gavels, columns, scales, law related images

```html
<!DOCTYPE html>
<html lang="en">
<head>
<meta charset="utf-8">
<title>Holloway Law Firm</title>
<link href="https://fonts.googleapis.com/css2?family=Noto+Serif:wght@400;700&family=Montserrat:wght@400;500;600&display=swap" rel="stylesheet">
<style>
:root{
  --red:#e3262a;
  --red-deep:#c52226;
  --ink:#1b1c20;
  --ink-deep:#131416;
  --text:#333;
  --muted:#555;
  --white:#fff;
  --serif:"Noto Serif", Georgia, serif;
  --sans:"Montserrat", Arial, sans-serif;
}
*{box-sizing:border-box;margin:0;padding:0}
html,body{width:1200px;height:3534px;overflow:hidden}
body{position:relative;background:var(--white);font-family:var(--sans);color:var(--text)}
.abs{position:absolute}
.ph{position:absolute;display:block}

/* hero */
.hero{position:absolute;left:0;top:0;width:1200px;height:532px;overflow:hidden}
.hero-panel{left:0;top:0;width:531px;height:532px;background:radial-gradient(circle at 45% 35%,#34363a 0%,#1d1e21 70%)}
.hero-photo{left:531px;top:76px;width:669px;height:456px;background:radial-gradient(circle at 40% 45%,#d8303a 0%,#8e1a22 35%,#2a0c0f 75%,#0c0c0e 100%)}
.topbar{left:531px;top:0;width:669px;height:38px;background:var(--white);font-size:11px;color:#222}
.topbar .item{position:absolute;top:8px;display:flex;align-items:center;gap:10px}
.ic-circle{width:22px;height:22px;border-radius:50%;background:#f3f3f3;display:flex;align-items:center;justify-content:center}
.nav{left:531px;top:38px;width:669px;height:38px;background:var(--red)}
.nav a{position:absolute;top:12px;color:var(--white);font-size:11px;font-weight:500;text-decoration:none;transform:translateX(-50%);letter-spacing:.2px}
.nav a.active{font-weight:600}
.logo{font-family:var(--serif);color:var(--red);font-weight:400;letter-spacing:1px;line-height:1.05}
.hero .logo{left:141px;top:40px;font-size:22px;text-align:center}
.eyebrow{font-family:var(--serif);color:var(--white);font-size:21px}
.hero-title{left:130px;top:190px;font-family:var(--serif);font-weight:700;color:var(--white);font-size:48px;line-height:54px}
.hero-title em{font-style:normal;color:var(--red)}
.hero-lead{left:130px;top:326px;width:390px;color:#e6e6e6;font-size:14px;line-height:22px}
.btn-white{left:130px;top:391px;width:110px;height:34px;background:var(--white);color:#111;font-size:11px;font-weight:600;display:flex;align-items:center;justify-content:center}
.arrow{position:absolute;width:28px;height:28px;border-radius:50%;background:#3a3b3e;display:flex;align-items:center;justify-content:center}

/* welcome */
.welcome-kicker{left:130px;top:640px;font-family:var(--serif);font-size:16px;color:#222}
.section-title{font-family:var(--serif);font-weight:700;font-size:36px;color:#1d1d1d;line-height:1.1}
.section-title span{color:var(--red)}
.welcome-text{left:130px;top:716px;width:385px;font-size:13px;line-height:20px;color:#333}
.btn-red{height:36px;background:var(--red-deep);color:var(--white);font-size:11px;font-weight:600;display:flex;align-items:center;justify-content:center;letter-spacing:.3px}

/* practice */
.practice{left:0;top:1004px;width:1200px;height:665px;background:linear-gradient(180deg,#2a2b2e 0%,#1c1d20 60%,#141517 100%)}
.practice-card{position:absolute;left:628px;width:443px;height:154px;background:var(--white);text-align:center}
.practice-card.featured{background:var(--red-deep)}
.practice-card h3{font-family:var(--serif);font-weight:400;font-size:19px;color:#1e1e1e;margin-top:72px}
.practice-card p{font-size:11.5px;line-height:17px;color:#444;width:350px;margin:10px auto 0}
.practice-card.featured h3,.practice-card.featured p{color:var(--white)}
.practice-card svg{position:absolute;left:50%;top:16px;transform:translateX(-50%)}

/* blog */
.date-badge{left:130px;top:2024px;width:52px;height:59px;background:var(--white);text-align:center;font-size:9px;font-weight:600;color:#111}
.date-badge .top{background:var(--red-deep);color:var(--white);height:36px;padding-top:5px;line-height:13px;font-size:9px;font-weight:500}
.date-badge .top b{font-size:10px}
.post-title{font-family:var(--serif);font-size:16px;color:#1d1d1d;line-height:21px}
.post-text{font-size:12px;line-height:18px;color:#444}
.post-date{font-size:10px;color:var(--red)}
.more{color:var(--red);font-weight:600;font-size:9.5px}
.thumb{width:140px;height:112px}

/* contact */
.contact{left:0;top:2301px;width:1200px;height:440px;background:var(--ink);overflow:hidden}
.contact-photo{left:627px;top:-103px;width:646px;height:646px;border-radius:50%;border:2px solid var(--red);background:linear-gradient(135deg,#f4f5f6 0%,#dfe3e6 55%,#3a3f4a 100%)}
.field{position:absolute;background:var(--white);font-size:10px;color:#333;padding:6px 12px}

/* testimonials */
.t-card{left:289px;top:2899px;width:620px;height:233px;background:var(--white);box-shadow:0 2px 14px rgba(0,0,0,.14)}
.t-quote{left:289px;top:2981px;width:620px;text-align:center;font-family:var(--serif);font-size:13.5px;line-height:21px;color:#333}
.t-source{left:289px;top:3064px;width:620px;text-align:center;font-family:var(--serif);font-weight:700;font-size:13px;color:var(--red)}
.dot-arrow{position:absolute;width:24px;height:24px;border-radius:50%;background:#222;display:flex;align-items:center;justify-content:center}

/* footer */
.footer{left:0;top:3206px;width:1200px;height:328px;background:var(--ink-deep)}
.footer h4{position:absolute;font-family:var(--serif);font-weight:700;font-size:19px;color:var(--white)}
.footer .rule{position:absolute;width:2px;height:20px;background:var(--white)}
.footer .vline{position:absolute;width:1px;background:#2a2b2e}
.f-text{position:absolute;font-size:11px;color:#e8e8e8;line-height:17px}
.f-link{position:absolute;left:751px;font-size:11px;color:#e8e8e8}
.social{position:absolute;top:3333px;width:28px;height:28px;border-radius:50%;background:var(--white)}
</style>
</head>
<body>

<!-- HERO -->
<section class="hero">
  <div class="abs hero-panel"></div>
  <div class="ph hero-photo" role="img" aria-label="Red car wrecked in a collision with shattered glass flying"></div>
  <svg class="abs" style="left:0;top:0" width="1200" height="532" aria-hidden="true">
    <polygon points="436,532 531,438 531,532" fill="#1c1d20"/>
    <polygon points="0,525 439,525 432,532 0,532" fill="#e3262a"/>
  </svg>
  <div class="abs topbar">
    <div class="item" style="left:234px">
      <span class="ic-circle"><svg width="11" height="11" viewBox="0 0 24 24"><path d="M6.6 10.8a15.1 15.1 0 0 0 6.6 6.6l2.2-2.2c.3-.3.7-.4 1-.2 1.1.4 2.3.6 3.6.6.6 0 1 .4 1 1V20c0 .6-.4 1-1 1C10.6 21 3 13.4 3 4c0-.6.4-1 1-1h3.5c.6 0 1 .4 1 1 0 1.3.2 2.5.6 3.6.1.3 0 .7-.2 1z" fill="#e3262a"/></svg></span>
      (615) 555-0142
    </div>
    <div class="item" style="left:362px">
      <span class="ic-circle"><svg width="11" height="9" viewBox="0 0 22 16"><rect width="22" height="16" rx="2" fill="#e3262a"/><path d="M1 2l10 7 10-7" stroke="#fff" stroke-width="2" fill="none"/></svg></span>
      office@hollowaylawfirm.example
    </div>
  </div>
  <nav class="abs nav">
    <a class="active" href="#" style="left:103px">HOME</a>
    <a href="#" style="left:193px">ABOUT US</a>
    <a href="#" style="left:307px">PRACTICE AREA</a>
    <a href="#" style="left:410px">NEWS</a>
    <a href="#" style="left:507px">CONTACT US</a>
  </nav>
  <div class="abs logo">HOLLOWAY<br>LAW FIRM</div>
  <div class="abs eyebrow" style="left:130px;top:158px">Don’t Lose</div>
  <h1 class="abs hero-title">What’s <em>Legally</em><br>Yours</h1>
  <p class="abs hero-lead">We strive to help our clients and do everything we can to make sure...</p>
  <div class="abs btn-white">GET STARTED</div>
  <span class="arrow" style="left:530px;top:410px"><svg width="8" height="10" viewBox="0 0 8 10"><path d="M6 1L2 5l4 4" stroke="#fff" stroke-width="1.5" fill="none"/></svg></span>
  <span class="arrow" style="left:564px;top:410px"><svg width="8" height="10" viewBox="0 0 8 10"><path d="M2 1l4 4-4 4" stroke="#fff" stroke-width="1.5" fill="none"/></svg></span>
</section>

<!-- WELCOME -->
<section>
  <div class="abs welcome-kicker">Welcome to</div>
  <h2 class="abs section-title" style="left:130px;top:658px;font-size:35px"><span>Holloway</span> Law Firm</h2>
  <p class="abs welcome-text">There are many law firms in Tennessee who claim to be trial lawyers, but their attorneys have never seen a courtroom.&nbsp; We have tried hundreds of cases to verdict and we have helped thousands of people in the Tennessee courts.&nbsp; We fight against billion dollar insurance companies, billion dollar corporations, and the State of Tennessee..and we win!</p>
  <div class="abs btn-red" style="left:130px;top:861px;width:110px">OUR TEAM</div>
  <div class="abs" style="left:566px;top:605px;width:103px;height:332px;background:var(--red-deep)"></div>
  <div class="ph" style="left:669px;top:605px;width:401px;height:325px;background:linear-gradient(160deg,#cfd6dc 0%,#9aa3ab 45%,#c23a33 75%,#7c2a25 100%)" role="img" aria-label="Paramedic in a red jacket giving first aid to an injured person outdoors"></div>
</section>

<!-- PRACTICE -->
<section class="abs practice" role="img" aria-label="Dark background of a tall building">
</section>
<h2 class="abs section-title" style="left:0;top:1048px;width:1200px;text-align:center;color:var(--white)"><span>Areas</span> of Practice</h2>
<div class="ph" style="left:130px;top:1163px;width:498px;height:415px;background:radial-gradient(circle at 35% 55%,#8a8e93 0%,#4d5156 45%,#1e2023 100%)" role="img" aria-label="Close-up of a damaged silver car front with headlight"></div>
<div class="practice-card" style="top:1126px">
  <svg width="44" height="44" viewBox="0 0 44 44" aria-hidden="true"><g transform="rotate(25 22 22)"><rect x="8" y="14" width="28" height="14" rx="4" fill="#c52226"/><rect x="13" y="9" width="18" height="8" rx="3" fill="#c52226"/><circle cx="14" cy="30" r="4" fill="#c52226"/><circle cx="30" cy="30" r="4" fill="#c52226"/></g></svg>
  <h3>Motor Vehicle Accidents</h3>
  <p>Sed ut perspiciatis unde omnis iste natus error sit voluptatem accusantium doloremque...</p>
</div>
<div class="practice-card featured" style="top:1293px">
  <svg width="44" height="44" viewBox="0 0 44 44" aria-hidden="true"><circle cx="26" cy="8" r="4" fill="#fff"/><path d="M24 13l-6 9 7 4-3 9M21 17l10 4" stroke="#fff" stroke-width="3" fill="none" stroke-linecap="round"/><path d="M4 38l8-14 8 14z" fill="#fff"/><rect x="11" y="29" width="2" height="5" fill="#c52226"/><path d="M24 40h16" stroke="#fff" stroke-width="2"/></svg>
  <h3>Slip and Fall Accidents</h3>
  <p>Sed ut perspiciatis unde omnis iste natus error sit voluptatem accusantium doloremque...</p>
</div>
<div class="practice-card" style="top:1461px">
  <svg width="44" height="44" viewBox="0 0 44 44" aria-hidden="true"><circle cx="20" cy="7" r="4" fill="#c52226"/><path d="M20 12l-2 12 6 6v10M18 24l-6 8M19 16l-8 4M20 16l9 3" stroke="#c52226" stroke-width="3" fill="none" stroke-linecap="round"/><ellipse cx="33" cy="32" rx="6" ry="4" fill="#c52226"/></svg>
  <h3>Dog Bites</h3>
  <p>Sed ut perspiciatis unde omnis iste natus error sit voluptatem accusantium doloremque...</p>
</div>

<!-- BLOG -->
<section>
  <h2 class="abs section-title" style="left:0;top:1732px;width:1200px;text-align:center"><span>Recent</span> Blog</h2>
  <div class="ph" style="left:130px;top:1802px;width:460px;height:281px;background:linear-gradient(120deg,#3c5a8c 0%,#cfdbe6 40%,#e9d9cc 60%,#9fb7cf 100%)" role="img" aria-label="Doctor bandaging a patient's injured foot"></div>
  <div class="abs date-badge"><div class="top"><b>21st</b><br>November</div><div style="padding-top:5px">2021</div></div>
  <h3 class="abs post-title" style="left:130px;top:2105px">Trucking Company Offers 6 Figure Settlement</h3>
  <p class="abs post-text" style="left:130px;top:2140px;width:460px">Sed ut perspiciatis unde omnis iste natus error sit voluptatem accusantium doloremque laudantium totam rem aperiam...</p>
  <div class="abs btn-red" style="left:130px;top:2191px;width:110px;background:var(--red-deep)">READ MORE</div>

  <div class="ph thumb" style="left:610px;top:1802px;background:linear-gradient(135deg,#3f5670 0%,#9aa6b2 50%,#d04030 80%,#7a7e84 100%)" role="img" aria-label="Crashed car on a road behind a red warning triangle"></div>
  <div class="abs post-date" style="left:769px;top:1806px">15th Nov, 2021</div>
  <h3 class="abs post-title" style="left:769px;top:1826px;width:280px">Insurance Company Pays for Facial Fractures</h3>
  <p class="abs post-text" style="left:769px;top:1876px;width:290px;font-size:11.5px">Sed ut perspiciatis unde omnis iste natus error sit voluptatem accusantium... <span class="more">READ MORE</span></p>

  <div class="ph thumb" style="left:610px;top:1958px;background:linear-gradient(135deg,#4d4a44 0%,#9c958a 50%,#e5e1da 70%,#6a655d 100%)" role="img" aria-label="Person helping an injured man with a bandaged leg"></div>
  <div class="abs post-date" style="left:769px;top:1974px">15th Nov, 2021</div>
  <h3 class="abs post-title" style="left:769px;top:1995px">DCS Chooses to Dismiss Case</h3>
  <p class="abs post-text" style="left:769px;top:2021px;width:290px;font-size:11.5px">Sed ut perspiciatis unde omnis iste natus error sit voluptatem accusantium... <span class="more">READ MORE</span></p>

  <div class="ph thumb" style="left:610px;top:2115px;background:linear-gradient(135deg,#f2f2f2 0%,#d9c0ad 50%,#e8d2c2 80%,#f5f5f5 100%)" role="img" aria-label="Close-up of a hand applying ointment to a wound on skin"></div>
  <div class="abs post-date" style="left:769px;top:2121px">15th Nov, 2021</div>
  <h3 class="abs post-title" style="left:769px;top:2141px;width:290px">Holloway Obtains Jury Verdict of 61 x Medical Bills</h3>
  <p class="abs post-text" style="left:769px;top:2188px;width:290px;font-size:11.5px">Sed ut perspiciatis unde omnis iste natus error sit voluptatem accusantium... <span class="more">READ MORE</span></p>
</section>

<!-- CONTACT -->
<section class="abs contact">
  <div class="ph contact-photo" role="img" aria-label="Two lawyers in business suits reviewing documents together in a bright office"></div>
  <h2 class="abs section-title" style="left:130px;top:59px;color:var(--white)"><span>Get In</span> Touch</h2>
  <div class="abs" style="left:130px;top:102px;font-size:11px;color:#cfcfcf">Get Free Internet access to enquery now</div>
  <div class="field" style="left:130px;top:136px;width:220px;height:36px">First Name:</div>
  <div class="field" style="left:358px;top:136px;width:221px;height:36px">Last Name:</div>
  <div class="field" style="left:130px;top:181px;width:220px;height:36px">Email:</div>
  <div class="field" style="left:358px;top:181px;width:221px;height:36px">Phone:</div>
  <div class="field" style="left:130px;top:226px;width:449px;height:102px">Comments:</div>
  <div class="abs btn-red" style="left:130px;top:338px;width:90px;height:37px;background:var(--red)">SEND</div>
</section>

<!-- TESTIMONIALS -->
<section>
  <h2 class="abs section-title" style="left:0;top:2806px;width:1200px;text-align:center">Testimonials</h2>
  <div class="abs t-card"></div>
  <div class="ph" style="left:562px;top:2860px;width:76px;height:76px;border-radius:50%;background:linear-gradient(160deg,#d9e6ea 0%,#8fb0b8 55%,#2d3b52 100%);border:3px solid #fff" role="img" aria-label="Portrait of the person quoted"></div>
  <p class="abs t-quote">Speak up for those who cannot speak for themselves, for the rights<br>of all who are destitute. Speak up and judge fairly; defend the rights of the<br>poor and needy.</p>
  <div class="abs t-source">PROVERBS</div>
  <span class="dot-arrow" style="left:278px;top:3005px"><svg width="8" height="10" viewBox="0 0 8 10"><path d="M6 1L2 5l4 4" stroke="#fff" stroke-width="2" fill="none"/></svg></span>
  <span class="dot-arrow" style="left:897px;top:3005px"><svg width="8" height="10" viewBox="0 0 8 10"><path d="M2 1l4 4-4 4" stroke="#fff" stroke-width="2" fill="none"/></svg></span>
</section>

<!-- FOOTER -->
<footer class="abs footer"></footer>
<div class="abs logo" style="left:130px;top:3316px;font-size:26px;text-align:center">HOLLOWAY<br>LAW FIRM</div>
<div class="abs" style="left:130px;top:3396px;font-size:9px;line-height:15px;color:#cfcfcf">Copyright © 2021 <span style="color:var(--red)">Holloway Law Firm.</span><br>All Rights Reserved.</div>

<div class="rule" style="left:430px;top:3292px"></div>
<h4 style="left:450px;top:3289px">Contacts</h4>
<div class="rule" style="left:705px;top:3292px"></div>
<h4 style="left:751px;top:3289px">Sitemap</h4>
<div class="rule" style="left:881px;top:3292px"></div>
<h4 style="left:941px;top:3289px">Follow Us</h4>
<div class="vline" style="left:431px;top:3320px;height:160px"></div>
<div class="vline" style="left:706px;top:3320px;height:160px"></div>
<div class="vline" style="left:882px;top:3320px;height:160px"></div>

<svg class="abs" style="left:449px;top:3333px" width="10" height="13" viewBox="0 0 10 13" aria-hidden="true"><path d="M5 0a5 5 0 0 1 5 5c0 3.5-5 8-5 8S0 8.5 0 5a5 5 0 0 1 5-5z" fill="#e3262a"/><circle cx="5" cy="5" r="2" fill="#131416"/></svg>
<div class="f-text" style="left:466px;top:3331px">1450 Maple Ridge Drive | Suite 210<br>Franklin, TN 37067</div>
<svg class="abs" style="left:449px;top:3393px" width="10" height="10" viewBox="0 0 24 24" aria-hidden="true"><path d="M6.6 10.8a15.1 15.1 0 0 0 6.6 6.6l2.2-2.2c.3-.3.7-.4 1-.2 1.1.4 2.3.6 3.6.6.6 0 1 .4 1 1V20c0 .6-.4 1-1 1C10.6 21 3 13.4 3 4c0-.6.4-1 1-1h3.5c.6 0 1 .4 1 1 0 1.3.2 2.5.6 3.6.1.3 0 .7-.2 1z" fill="#e3262a"/></svg>
<div class="f-text" style="left:466px;top:3390px">(615) 555-0142</div>
<svg class="abs" style="left:449px;top:3436px" width="11" height="8" viewBox="0 0 22 16" aria-hidden="true"><rect width="22" height="16" rx="2" fill="#e3262a"/><path d="M1 2l10 7 10-7" stroke="#131416" stroke-width="2" fill="none"/></svg>
<div class="f-text" style="left:466px;top:3432px">office@hollowaylawfirm.example</div>

<div class="f-link" style="top:3331px">Home</div>
<div class="f-link" style="top:3357px">About Us</div>
<div class="f-link" style="top:3382px">Practice Area</div>
<div class="f-link" style="top:3408px">News</div>
<div class="f-link" style="top:3433px">Contact Us</div>

<span class="social" style="left:940px"></span>
<span class="social" style="left:974px"></span>
<span class="social" style="left:1008px"></span>
<span class="social" style="left:1042px"></span>

</body>
</html>
```